Pressure Washing Hog Confinements

We clean and disinfect Hog confinements in-order to receive new pigs.

Needs to emphasis Clean Healthy barns (pigs), work done in timely manner, 100% satisfied, Bio-security rules followed. I do not have specific colors, no logo's.

Contact Information will be sent once design is agreed on.
Business Name - Barlow & Daughters Power Washing
Phone Number - Send latter
E-mail - Send latter
Web Address - Send latter

Target Market(s)

Farmers

Industry/Entity Type

Business

Requirements
Must have
• We are Insured
Bio-Security
100% Satisfied
Water Conservation

Size - 2 sided Postcard 8.5" x 5.5"
Nice to have
• I want to emphasize healthy and happy pigs because of a quality job done. Picture of pigs dose not need to be used but may be just an example.

Also attached is picture of a barn I would like to see used. on the back side. Every owner seeing this will know this is a hog barn and have an idea what we do.

```html
<!DOCTYPE html>
<html lang="en">
<head>
<meta charset="UTF-8">
<title>Barlow &amp; Daughters Power Washing – Hog Confinement Postcard</title>
<link rel="stylesheet" href="https://fonts.googleapis.com/css2?family=Open+Sans:ital,wght@0,400;0,600;0,800;1,400&display=swap">
<style>
  :root {
    --charcoal: #3b4045;
    --charcoal-deep: #2f3337;
    --slate-text: #3e4347;
    --lime: #8cc63f;
    --lime-light: #b5dc6e;
    --mist: #e9eaea;
    --mist-dark: #c9cccd;
    --white: #ffffff;
    --pig-pink: #e8b9a9;
    --barn-grey: #b7bcbf;
  }
  * { margin: 0; padding: 0; box-sizing: border-box; }
  html, body { width: 1200px; height: 778px; overflow: hidden; background: var(--white); }
  .postcard {
    position: relative;
    width: 1200px;
    height: 778px;
    overflow: hidden;
    font-family: "Open Sans", Arial, sans-serif;
    background: linear-gradient(180deg, #f3f3f3 0%, var(--mist) 55%, var(--mist-dark) 100%);
  }
  .hero-photo {
    position: absolute;
    left: 430px; top: 0;
    width: 770px; height: 470px;
    background:
      radial-gradient(ellipse 240px 200px at 380px 170px, var(--pig-pink) 0%, #ddb2a4 45%, rgba(221,178,164,0) 100%),
      linear-gradient(180deg, #d3d7d9 0%, var(--barn-grey) 60%, #9fa6aa 100%);
    -webkit-mask-image: linear-gradient(90deg, transparent 0%, #000 28%);
            mask-image: linear-gradient(90deg, transparent 0%, #000 28%);
  }
  .brand-block {
    position: absolute;
    left: 0; top: 0;
    width: 516px; height: 146px;
    background: var(--charcoal);
    padding: 14px 0 0 34px;
    color: var(--white);
  }
  .brand-name {
    font-size: 40px;
    font-weight: 400;
    letter-spacing: 1px;
    line-height: 1.1;
  }
  .brand-service {
    color: var(--lime);
    font-size: 26px;
    font-weight: 400;
    line-height: 1.15;
    margin-left: 70px;
    margin-top: 4px;
  }
  .brand-tagline {
    color: var(--lime);
    font-size: 22px;
    line-height: 1.1;
    margin-left: 74px;
  }
  .brand-rule {
    position: absolute;
    left: 0; top: 150px;
    width: 580px; height: 6px;
    background: linear-gradient(90deg, var(--lime) 0%, var(--lime) 80%, rgba(140,198,63,0) 100%);
  }
  .headline {
    position: absolute;
    left: 42px; top: 218px;
    color: var(--slate-text);
    font-size: 52px;
    font-weight: 400;
    line-height: 1.2;
    letter-spacing: 0.5px;
  }
  .headline em { font-style: italic; }
  .swoosh {
    position: absolute;
    left: 0; top: 0;
    width: 1200px; height: 778px;
  }
  .piglets-photo {
    position: absolute;
    left: 780px; top: 574px;
    width: 420px; height: 204px;
    background: linear-gradient(160deg, #e9c2b3 0%, #d9a896 50%, #b49081 100%);
    border-top-left-radius: 6px;
  }
  .insured {
    position: absolute;
    left: 736px; top: 474px;
    font-size: 46px;
    color: var(--white);
    font-weight: 400;
  }
  .insured .accent { color: var(--lime); }
  .promises {
    position: absolute;
    left: 42px; top: 555px;
    color: var(--white);
    line-height: 1.1;
  }
  .promise { font-size: 48px; font-weight: 400; }
  .promise-key {
    font-size: 66px;
    font-weight: 800;
    color: var(--lime);
    line-height: 1.05;
  }
</style>
</head>
<body>
<main class="postcard">
  <div class="hero-photo" role="img" aria-label="Photo of a clean, healthy pig looking through barn gate bars"></div>

  <header class="brand-block">
    <div class="brand-name">BARLOW &amp; DAUGHTERS</div>
    <div class="brand-service">HOG CONFINMENT</div>
    <div class="brand-tagline">cleaning and disinfection</div>
  </header>
  <div class="brand-rule"></div>

  <h1 class="headline">WORK COMPLETED<br>IN <em>TIMELY</em> MANNER</h1>

  <svg class="swoosh" viewBox="0 0 1200 778" aria-hidden="true">
    <path d="M0,400 C320,380 560,470 800,410 C960,370 1080,345 1200,340 L1200,380 C1080,385 960,405 820,445 C600,500 300,425 0,450 Z" fill="#ffffff" opacity="0.75"/>
    <path d="M0,440 C300,415 580,500 810,440 C960,400 1080,378 1200,372 L1200,778 L0,778 Z" fill="var(--lime)"/>
    <path d="M0,462 C300,440 590,520 820,460 C965,422 1080,398 1200,392 L1200,778 L0,778 Z" fill="var(--charcoal)"/>
    <path d="M0,520 C260,500 520,560 700,640 C760,670 790,720 800,778 L0,778 Z" fill="var(--charcoal-deep)" opacity="0.55"/>
  </svg>

  <div class="piglets-photo" role="img" aria-label="Photo of a group of healthy piglets on a clean barn floor"></div>

  <p class="insured">We Are <span class="accent">Insured</span></p>

  <section class="promises">
    <p class="promise">Bio-Security</p>
    <p class="promise-key">100% Satisfied</p>
    <p class="promise">Water Conservation</p>
  </section>
</main>
</body>
</html>
```